Business Card for a new businees.

need a very good business for a new company based in Riverside California call Levy Lantern LLC. We help client file taxes, resolve tax debt and attain peace of mind We help people nationwide solve Tax problems. We help with Installment agreements, Offers in Compromise, Partial Pay Installment Agreements, Currently Not Collectible status, Liens and Levy Removal, Garnishment removal. We offer individualized services

Target Market(s)

Any one with Tax Problems nationwide. My clients span across age, occupation etc

Contact Information for Business Card

Card must be attractive and have enough information to let client know we care and call us

Colors

Designer to choose colors to be used in the design.

Requirements
Must have
• the basics and then surprise me
Nice to have
• surprise m

```html
<!DOCTYPE html>
<html lang="en">
<head>
<meta charset="utf-8">
<title>Levy Lantern LLC — Business Card</title>
<link href="https://fonts.googleapis.com/css2?family=Oswald:wght@500;600&family=Roboto+Condensed:wght@400;500&display=swap" rel="stylesheet">
<style>
  :root {
    --stage: #d9d9d9;
    --card-light: #ffffff;
    --card-dark: #231f1e;
    --gold: #c9a81a;
    --gold-bright: #e6c531;
    --gold-deep: #8f7a16;
  }
  * { box-sizing: border-box; margin: 0; padding: 0; }
  html, body { width: 1200px; height: 786px; overflow: hidden; }
  body {
    background: var(--stage);
    font-family: "Roboto Condensed", Arial, sans-serif;
    position: relative;
  }
  .card {
    position: absolute;
    top: 245px;
    width: 520px;
    height: 297px;
    border-radius: 16px;
    box-shadow: 0 10px 30px rgba(0,0,0,0.18);
    overflow: hidden;
  }
  .card--front { left: 60px; background: var(--card-light); }
  .card--back  { left: 620px; background: var(--card-dark); }

  .person { position: absolute; left: 36px; top: 44px; }
  .person__name {
    font-family: "Oswald", sans-serif;
    font-weight: 600;
    font-size: 22px;
    letter-spacing: 0.5px;
    color: var(--gold-deep);
  }
  .person__title { font-size: 13px; color: var(--gold-deep); margin-top: 2px; }

  .contact { position: absolute; left: 36px; top: 142px; list-style: none; }
  .contact__item {
    display: flex; align-items: center; gap: 8px;
    font-size: 13px; color: var(--gold-deep); margin-bottom: 6px;
  }
  .contact__item svg { width: 12px; height: 12px; fill: var(--gold); }

  .address {
    position: absolute; left: 300px; top: 218px;
    font-size: 13px; line-height: 1.35; color: var(--gold-deep); font-style: normal;
  }

  .brand { position: absolute; text-align: left; }
  .card--front .brand { left: 250px; top: 48px; }
  .card--back .brand { left: 70px; top: 88px; }
  .brand__name {
    display: flex; align-items: center; gap: 10px;
    font-family: "Oswald", sans-serif;
    font-weight: 600;
    color: var(--gold);
    line-height: 1;
  }
  .brand__dot { border-radius: 50%; background: var(--gold); flex: none; }
  .card--front .brand__name { font-size: 38px; }
  .card--front .brand__dot { width: 16px; height: 16px; }
  .card--back .brand__name { font-size: 52px; color: var(--gold-bright); }
  .card--back .brand__dot { width: 22px; height: 22px; background: var(--gold-bright); }
  .brand__rule { height: 3px; background: var(--gold); margin: 10px 0 6px; width: 100%; }
  .card--back .brand__rule { background: var(--gold-bright); }
  .brand__tag {
    font-size: 10px; letter-spacing: 3.5px; text-transform: uppercase;
    color: var(--gold-deep); font-weight: 500;
  }
  .brand__sub {
    font-size: 9px; text-transform: uppercase; color: var(--gold-deep); margin-top: 4px; letter-spacing: 0.3px;
  }
  .card--back .brand__tag { font-size: 13px; color: var(--gold); }
  .card--back .brand__sub { font-size: 11px; color: var(--gold); }
</style>
</head>
<body>

<section class="card card--front" aria-label="Business card front">
  <div class="person">
    <p class="person__name">JORDAN HALE</p>
    <p class="person__title">General Manager</p>
  </div>

  <ul class="contact">
    <li class="contact__item">
      <svg viewBox="0 0 24 24" aria-hidden="true"><path d="M6.6 10.8a15.1 15.1 0 0 0 6.6 6.6l2.2-2.2c.3-.3.7-.4 1-.2 1.1.4 2.3.6 3.6.6.6 0 1 .4 1 1V20c0 .6-.4 1-1 1A17 17 0 0 1 3 4c0-.6.4-1 1-1h3.5c.6 0 1 .4 1 1 0 1.3.2 2.5.6 3.6.1.3 0 .7-.2 1z"/></svg>
      951-555-0148
    </li>
    <li class="contact__item">
      <svg viewBox="0 0 24 24" aria-hidden="true"><path d="M2 5h20v14H2zm2 2v.5l8 5 8-5V7l-8 5z"/></svg>
      info@levylantern.com
    </li>
    <li class="contact__item">
      <svg viewBox="0 0 24 24" aria-hidden="true"><path d="M12 2a10 10 0 1 0 0 20 10 10 0 0 0 0-20zm6.9 9h-3a15 15 0 0 0-1.3-5.6A8 8 0 0 1 18.9 11zM12 4c1 1.3 1.8 3.9 1.9 7h-3.8C10.2 7.9 11 5.3 12 4zM9.4 5.4A15 15 0 0 0 8.1 11h-3a8 8 0 0 1 4.3-5.6zM5.1 13h3a15 15 0 0 0 1.3 5.6A8 8 0 0 1 5.1 13zM12 20c-1-1.3-1.8-3.9-1.9-7h3.8c-.1 3.1-.9 5.7-1.9 7zm2.6-1.4a15 15 0 0 0 1.3-5.6h3a8 8 0 0 1-4.3 5.6z"/></svg>
      www.levylantern.com
    </li>
  </ul>

  <div class="brand">
    <p class="brand__name"><span class="brand__dot"></span>Levy Lantern</p>
    <div class="brand__rule"></div>
    <p class="brand__tag">Tax Relief. Tax Returns.</p>
    <p class="brand__sub">Your tax advocates. Peace of mind, nationwide</p>
  </div>

  <address class="address">
    2450 Orchard Ave. Ste 110<br>
    Riverside, CA 92503
  </address>
</section>

<section class="card card--back" aria-label="Business card back">
  <div class="brand">
    <p class="brand__name"><span class="brand__dot"></span>Levy Lantern</p>
    <div class="brand__rule"></div>
    <p class="brand__tag">Tax Relief. Tax Returns.</p>
    <p class="brand__sub">Your tax advocates. Peace of mind, nationwide</p>
  </div>
</section>

</body>
</html>
```